MapleTideEvents
MaplTideEvents - Business Card/Stationary
I need double sided standard sized Business Card [3.5" x 2"]
we use "segan" on the website - feel free to expirement, we are not set on one yet
Professional
Nadia Feltwick
Director of Logistics
4187 Birchwell Hollow Lane
Brookhaven, WA 95182
nadia@mapletide.com
www.mapletide.com
-Please look at our website: www.mapletide.com
We would like the business card to replicate the look of the website.
-As noted earlier, we have not settled on a font yet, please feel free to be creative with the styles
- Font used on website = segan (or similar)
-Double-Sided is "optional" we would also like to see just some single sided versions as well.
- Regular standard size business card
we wanted to explore the option of having a double sided card. This is not mandatory, but if there is a creative design for it, this would be great.
Logo - Icon ONLY
Logo - Icon with Title

```html
<!DOCTYPE html>
<html lang="en">
<head>
<meta charset="utf-8">
<title>MapleTideEvents Business Card</title>
<link rel="stylesheet" href="https://fonts.googleapis.com/css2?family=Open+Sans:wght@400;600;700&display=swap">
<style>
  :root {
    --page: #ffffff;
    --blue-deep: #1a4f93;
    --blue-mid: #1f6db6;
    --blue-light: #2b8fd4;
    --gray: #5c5f63;
    --white: #ffffff;
    --brand: #2a86c8;
  }
  html, body {
    margin: 0;
    width: 1200px;
    height: 1002px;
    overflow: hidden;
    background: var(--page);
    font-family: "Open Sans", Arial, sans-serif;
  }
  .sheet { position: relative; width: 1200px; height: 1002px; }
  .card {
    position: absolute;
    top: 77px;
    width: 486px;
    height: 832px;
    overflow: hidden;
    box-shadow: 0 6px 14px rgba(0,0,0,0.25);
  }
  .card-front { left: 82px; background: var(--white); }
  .card-back {
    left: 644px;
    background: linear-gradient(160deg, var(--blue-deep) 0%, var(--blue-mid) 45%, var(--blue-light) 100%);
  }
  .front-art { position: absolute; inset: 0; }
  .contact {
    position: absolute;
    top: 0; left: 0; right: 0;
    text-align: center;
    color: var(--white);
  }
  .name { margin: 36px 0 0; font-size: 36px; font-weight: 700; line-height: 46px; }
  .role { margin: 2px 0 0; font-size: 19px; line-height: 26px; }
  .details { margin: 82px 0 0; font-size: 20px; line-height: 33px; }
  .details p { margin: 0; }
  .brand {
    display: flex;
    align-items: center;
    gap: 10px;
    font-weight: 400;
    white-space: nowrap;
  }
  .brand-mark { display: block; flex: none; }
  .front-brand {
    position: absolute;
    left: 36px;
    top: 690px;
    font-size: 38px;
    color: var(--brand);
  }
  .front-brand .brand-mark { width: 76px; height: 76px; background: var(--brand); }
  .back-brand {
    position: absolute;
    left: 82px;
    top: 398px;
    font-size: 27px;
    color: var(--white);
  }
  .back-brand .brand-mark { width: 60px; height: 60px; background: var(--white); }
  .back-url {
    position: absolute;
    top: 790px;
    margin: 0;
    left: 0; right: 0;
    text-align: center;
    color: var(--white);
    font-size: 19px;
  }
</style>
</head>
<body>
<main class="sheet">
  <section class="card card-front" aria-label="Card front">
    <svg class="front-art" viewBox="0 0 486 832" width="486" height="832" aria-hidden="true">
      <defs>
        <linearGradient id="frontBlue" x1="0" y1="0" x2="0" y2="1">
          <stop offset="0" stop-color="#1a4f93"/>
          <stop offset="0.55" stop-color="#1f6db6"/>
          <stop offset="1" stop-color="#2b8fd4"/>
        </linearGradient>
        <linearGradient id="waveGreen" x1="0" y1="0" x2="1" y2="0">
          <stop offset="0" stop-color="#1f7a6a"/>
          <stop offset="0.5" stop-color="#3aa489"/>
          <stop offset="1" stop-color="#1f7a6a"/>
        </linearGradient>
      </defs>
      <rect width="486" height="832" fill="url(#frontBlue)"/>
      <path d="M0 480 C150 380 340 360 486 420 L486 832 L0 832 Z" fill="url(#waveGreen)"/>
      <path d="M0 520 C170 425 360 440 486 625 L486 832 L0 832 Z" fill="#5c5f63"/>
      <path d="M0 532 C170 440 360 460 486 645 L486 832 L0 832 Z" fill="#ffffff"/>
    </svg>
    <div class="contact">
      <h1 class="name">Nadia Feltwick</h1>
      <p class="role">Director of Logistics</p>
      <div class="details">
        <p>4187 Birchwell Hollow Lane</p>
        <p>Brookhaven, WA 95182</p>
        <p>Phone: (555) 304.2178</p>
        <p>Email: nadia@mapletide.com</p>
        <p>www.mapletide.com</p>
      </div>
    </div>
    <div class="brand front-brand">
      <span class="brand-mark"></span>
      <span class="brand-name">MapleTideEvents</span>
    </div>
  </section>

  <section class="card card-back" aria-label="Card back">
    <div class="brand back-brand">
      <span class="brand-mark"></span>
      <span class="brand-name">MapleTideEvents</span>
    </div>
    <p class="back-url">www.mapletide.com</p>
  </section>
</main>
</body>
</html>
```